Stationery for Villa Marisol Design Hotel**

Who we are:

Wander on an isolated beach while breathing in the fresh, salty, sea air. Listen to the warm Pacific wind rustling through green palm trees as you walk to a pristine lagoon. Feel the delicious warmth of the sun kiss your skin; the beach is yours. At Villa Marisol you can experience a vacation in undisturbed, natural beauty. We have created a place for you to find new strength, relaxation, and inner harmony. We offer total rest to the experienced traveler from all over the world.

We are a brand new and smartly built design-hotel (under construction) close to a unique beach and a fantastic surf spot in Huatulco, Southwest Mexico.

As you can see in the attachments, we do have an established corporate design, but as for now still need a format for booklets for information around our hotel and things to do in the area, important numbers (we fill in the content for that one).

Our corporate colors:
green #64b445, brown #b07043, blue #0ab7cf, yellow # f9b02a and #fcc01a, navy #444f69
Corporate fonts:
Krub and Miller Banner.
For further information access:
www.villamarisol-example.mx
https://slidevault.example/view/QmWpLxTe8HnKdYcRuZsJ/

Social Media: VillaMarisol

Industry/Entity Type

Hotel

Font styles to use
Other font styles liked:
• Krub, Miller Banner

Requirements
Must have
• Stick to Logo Design, defined corporate elements, logo, colors, fonts and general touch and feel
Nice to have
• Who we are:

Our corporate colors:
Corporate fonts:
Krub and Miller Banner.
www.villamarisol-example.mx

Social Media: VillaMarisol

```html
<!DOCTYPE html>
<html lang="en">
<head>
<meta charset="utf-8">
<title>Villa Marisol – Envelope Stationery</title>
<link href="https://fonts.googleapis.com/css2?family=Krub:wght@500&family=Libre+Baskerville&display=swap" rel="stylesheet">
<style>
  :root {
    --bg: #a9acba;
    --paper: #f6f6f6;
    --paper-shade: #ebebeb;
    --green: #64b445;
    --brown: #b07043;
    --blue: #0ab7cf;
    --yellow: #f9b02a;
    --gold: #d9a22a;
    --navy: #444f69;
    --teal-liner: #3f7f93;
    --leaf-tint: #dfe9d2;
  }
  html, body {
    margin: 0;
    width: 1200px;
    height: 950px;
    overflow: hidden;
    background: var(--bg);
  }
  .canvas {
    position: relative;
    width: 1200px;
    height: 950px;
  }
  .envelope {
    position: absolute;
    left: 100px;
    width: 1000px;
    height: 400px;
    background: var(--paper);
    box-shadow: 0 4px 14px rgba(40, 44, 60, 0.25);
  }
  .envelope--front { top: 45px; overflow: hidden; }
  .envelope--back { top: 500px; }

  .brand {
    position: absolute;
    left: 48px;
    top: 48px;
    display: flex;
    flex-direction: column;
    gap: 10px;
  }
  .brand__mark {
    display: flex;
    align-items: center;
    gap: 12px;
  }
  .brand__square {
    width: 22px;
    height: 22px;
    background: var(--gold);
  }
  .brand__name {
    font-family: "Krub", sans-serif;
    font-weight: 500;
    font-size: 24px;
    letter-spacing: 1.5px;
    text-transform: uppercase;
    color: var(--gold);
  }
  .brand__address {
    font-family: "Libre Baskerville", serif;
    font-size: 13px;
    line-height: 1.45;
    color: var(--green);
    margin: 0 0 0 34px;
  }

  .leaf-art {
    position: absolute;
    right: 20px;
    top: 40px;
    width: 250px;
    height: 230px;
    border-radius: 50% 45% 40% 55%;
    background: radial-gradient(circle at 45% 45%, #d6e5c6, var(--leaf-tint) 70%, rgba(223,233,210,0) 100%);
  }

  .edge-band {
    position: absolute;
    left: 0;
    bottom: 0;
    width: 100%;
    height: 8px;
    display: flex;
  }
  .edge-band__segment { height: 100%; }
  .edge-band__segment--yellow { flex: 0 0 35%; background: var(--yellow); }
  .edge-band__gap { flex: 0 0 0.6%; background: var(--paper); }
  .edge-band__segment--green { flex: 0 0 42%; background: #8fd063; }
  .edge-band__segment--navy { flex: 1; background: var(--teal-liner); }

  .envelope__drawing { position: absolute; inset: 0; width: 100%; height: 100%; }
</style>
</head>
<body>
<main class="canvas">

  <section class="envelope envelope--front" aria-label="Envelope front">
    <div class="brand">
      <div class="brand__mark">
        <span class="brand__square"></span>
        <span class="brand__name">Villa Marisol</span>
      </div>
      <p class="brand__address">Playa Serena, Costa Azul,<br>Oaxaca, Mexico</p>
    </div>
    <div class="leaf-art" role="img" aria-label="Faint pale green monstera leaf illustration"></div>
    <div class="edge-band">
      <span class="edge-band__segment edge-band__segment--yellow"></span>
      <span class="edge-band__gap"></span>
      <span class="edge-band__segment edge-band__segment--green"></span>
      <span class="edge-band__gap"></span>
      <span class="edge-band__segment edge-band__segment--navy"></span>
    </div>
  </section>

  <section class="envelope envelope--back" aria-label="Envelope back with open flap">
    <svg class="envelope__drawing" viewBox="0 0 1000 400" preserveAspectRatio="none">
      <path class="liner" role="img" aria-label="Teal envelope liner with geometric pattern"
            d="M0 110 Q0 0 40 0 L960 0 Q1000 0 1000 40 L1000 110 Q960 70 920 100 L80 100 Q40 70 0 110 Z"
            fill="var(--teal-liner)"/>
      <path d="M0 400 L0 130 Q10 100 60 100 L140 100 Q110 110 100 150 L100 400 Z"
            fill="var(--paper-shade)" opacity="0.6"/>
      <path d="M1000 400 L1000 130 Q990 100 940 100 L860 100 Q890 110 900 150 L900 400 Z"
            fill="var(--paper-shade)" opacity="0.6"/>
      <path d="M80 100 L920 100" stroke="#e2e2e2" stroke-width="1.5" fill="none"/>
      <path d="M100 150 Q100 130 130 120" stroke="#dcdcdc" stroke-width="1.5" fill="none"/>
      <path d="M900 150 Q900 130 870 120" stroke="#dcdcdc" stroke-width="1.5" fill="none"/>
    </svg>
  </section>

</main>
</body>
</html>
```